Greek God inspired Air Freshen needs Foil Package Design

We are Lantern of Meridia. We sell car air fresheners inspired by Ancient Greece. We currently sell 5 proprietary scents. You can see them here: https://www.shopvarel.example/Freshener-Natural-Essential-Lantern-Meridia/dp/Q7K2MXR4PL
These are luxury air fresheners sold in awesome packages. 100% essential oils blended and bottled in the USA.
We need your help! We want to sell an additional line of scents. This line will be called "The Tidal Series" - or, The Tidal Series by Lantern of Meridia. This collection's theme will be - "The aromas you love, refined by the Fates."
These new products will be takes on well know colognes and perfumes.
We will start with 3 new products:
Halvir – inspired by Brisamel by Tolvane
Lemituna – inspired by Marindel by Quell
Pelund – inspired by Nevra by Faskow
Our original 5 products are packaged in tubes and bottled in a luxury black 8ml bottle (see attached and the link above). The "Tidal Series" will also have the same bottles, BUT, we want to package them in MYLAR FOIL BAGS. They will be 10x7cm (template attached).
What we need from you guys .... 3 designs. Front of the bag ONLY. One for each:
You have free reign, however the following items must be met:
The designs must be min 300 dpi.
Must include: "Tidal Series by Lantern of Meridia"
Must include: Lantern of Meridia Logo (attached)
Must include the words: "Car Air Fresheners"
Must marry well with our current imagery: https://www.shopvarel.example/Freshener-Natural-Essential-Lantern-Meridia/dp/Q7K2MXR4PL
Don't necessarily need to mention the cologne that our product is inspired by, however, perhaps consider use some fonts/pattern/s shadows of the Tolvane/Brsiamel bottle "shape" as an example.
Keep in mind, you are only designing the front of the packages. We will complete the back. The back will have the brand story, instructions, UPC, ingredients.
Our thoughts on using foil mylar bags: 1. We sell online 2. They will stand out from the others 3. Gives you/designer more space/opportunity to convey the product/message 4. We believe mock-ups/photos of the bags will look great on our listing
Please contact with any questions.

```html
<!DOCTYPE html>
<html lang="en">
<head>
<meta charset="utf-8">
<title>Halvir – Tidal Series – Lantern of Meridia</title>
<link rel="stylesheet" href="https://fonts.googleapis.com/css2?family=EB+Garamond:wght@400;500&family=Josefin+Sans:wght@400&display=swap">
<style>
  :root {
    --page: #e8e8e8;
    --foil-silver: #d9d9d9;
    --foil-silver-light: #eeeeee;
    --foil-black: #060606;
    --gold: #a88a37;
    --gold-light: #c4a650;
    --gold-text: #b09a56;
    --ink: #111111;
  }
  * { margin: 0; padding: 0; box-sizing: border-box; }
  html, body { width: 1200px; height: 1200px; overflow: hidden; background: var(--page); }
  .canvas { position: relative; width: 1200px; height: 1200px; background: var(--page); }
  .pouch { position: absolute; left: 0; top: 0; width: 1200px; height: 1200px; }
  .pouch-text { position: absolute; left: 286px; width: 626px; text-align: center; }
  .category {
    top: 494px;
    font-family: "EB Garamond", serif;
    font-size: 28px;
    line-height: 36px;
    letter-spacing: 1px;
    color: var(--gold-text);
  }
  .product-plate {
    position: absolute;
    left: 434px; top: 579px; width: 322px; height: 103px;
    background: linear-gradient(180deg, var(--gold-light), var(--gold));
    display: flex; align-items: center; justify-content: center;
  }
  .product-plate::before {
    content: ""; position: absolute; inset: 6px;
    border: 2px solid var(--ink);
  }
  .product-name {
    font-family: "Josefin Sans", sans-serif;
    font-size: 50px;
    letter-spacing: 2px;
    color: var(--ink);
    padding-top: 8px;
  }
  .collection {
    top: 700px;
    font-family: "EB Garamond", serif;
    font-size: 40px;
    line-height: 48px;
    color: var(--gold-text);
  }
  .maker { top: 810px; display: flex; flex-direction: column; align-items: center; gap: 14px; }
  .maker-mark { width: 90px; height: 90px; border: 3px solid var(--gold); border-radius: 50%; }
  .maker-name {
    font-family: "EB Garamond", serif;
    font-size: 17px;
    letter-spacing: 1px;
    color: var(--gold-text);
  }
</style>
</head>
<body>
<main class="canvas">
  <svg class="pouch" viewBox="0 0 1200 1200" xmlns="http://www.w3.org/2000/svg">
    <defs>
      <clipPath id="pouch-shape">
        <rect x="286" y="210" width="626" height="813" rx="4"/>
      </clipPath>
      <linearGradient id="silver-foil" x1="0" y1="0" x2="1" y2="1">
        <stop offset="0" stop-color="var(--foil-silver)"/>
        <stop offset="0.5" stop-color="var(--foil-silver-light)"/>
        <stop offset="1" stop-color="var(--foil-silver)"/>
      </linearGradient>
    </defs>
    <g clip-path="url(#pouch-shape)">
      <rect class="foil-top" x="286" y="210" width="626" height="442" fill="url(#silver-foil)"/>
      <rect class="foil-bottom" x="286" y="652" width="626" height="371" fill="var(--foil-black)"/>
      <path class="key-border" role="img" aria-label="Gold Greek key border pattern running in a ring around the pouch"
            fill="var(--gold)" fill-rule="evenodd"
            d="M597 177 a440 440 0 1 0 0.01 0 Z M597 262 a355 355 0 1 0 0.01 0 Z"/>
    </g>
  </svg>

  <p class="pouch-text category">CAR AIR<br>FRESHENERS</p>
  <div class="product-plate"><span class="product-name">HALVIR</span></div>
  <p class="pouch-text collection">TIDAL SERIES</p>
  <div class="pouch-text maker">
    <span class="maker-mark"></span>
    <span class="maker-name">LANTERN OF MERIDIA</span>
  </div>
</main>
</body>
</html>
```